Jolly Snaps - Photobooth hire

Photobooth flyer

We have just got our new photobooth and are ready to get the marketing side of things done! Our flyer needs to attract weddings, birthdays, corporate events, hens nights ect. For the winning flyer I would also like to follow up with the designer and get started with logo, business cards, web designs, car stickers etc. The flyer needs include this information

prices. $450 - 3 hrs $550 - 4 hrs $650 - 5 hrs. For extra time, additional payment can be made on the night. Our booths are also built with the flexibility to break down into smaller booths suitable for children. Prices start from $250 for kids parties and day time events.

All packages include
Unlimited prints
2 photo strips, one for you and one for friend.
Choice of different filters
Green screen technology - optional
Photobooth attendant
Use of cheeky props.

Call us for information and prices on additional items like photo albums, magnets, personalized photo strips, and more :)
0461927584

Feel free to change wording and add some character ;P

I would also like there to be sort of like a photostrip wave that I can add our photos. We will have them in a week :)
Thankyou for your time, am really looking forward to seeing what you come up with!!

Marketing

Sans Serif

8869ae

• I have uploaded a couple of flyers that I have come across and really like.. I like how the background is grey with some bold colour coming through.
• It also makes it hard because I don't have a logo.. But even in the heading, photobooth, I was thinking maybe a moustache underneath booth. Or even a cute little camera in one of the O's.

```html
<!DOCTYPE html>
<html lang="en">
<head>
<meta charset="utf-8">
<title>Jolly Snaps – Photobooth Flyer</title>
<link rel="stylesheet" href="https://fonts.googleapis.com/css2?family=Archivo:wght@800;900&family=Lato:wght@400;700;900&family=Oswald:wght@400;500;700&display=swap">
<style>
  :root {
    --purple: #8869ae;
    --purple-light: #a088c4;
    --purple-deep: #6e4f98;
    --price-purple: #7657a2;
    --charcoal: #2b2b2b;
    --charcoal-light: #4a4a4a;
    --ink: #141414;
    --white: #ffffff;
    --price-green: #3d5a12;
    --pill-text: #3a3a3a;
  }
  * { box-sizing: border-box; margin: 0; padding: 0; }
  html, body { width: 915px; height: 1200px; overflow: hidden; background: var(--white); }
  .flyer { position: relative; width: 915px; height: 1200px; overflow: hidden; font-family: "Lato", sans-serif; }

  .top-band {
    position: absolute; left: 0; top: 0; width: 100%; height: 362px;
    background: radial-gradient(ellipse at 60% 30%, var(--charcoal-light) 0%, var(--charcoal) 55%, #1c1c1c 100%);
  }
  .main-band {
    position: absolute; left: 0; top: 366px; width: 100%; height: 764px;
    border-top: 4px solid var(--white);
    background: radial-gradient(ellipse at 50% 55%, var(--purple-light) 0%, var(--purple) 55%, var(--purple-deep) 100%);
  }
  .footer-band {
    position: absolute; left: 0; top: 1130px; width: 100%; height: 70px;
    border-top: 5px solid var(--white);
    background: linear-gradient(90deg, #111 0%, #2e2e2e 50%, #111 100%);
    display: flex; align-items: center; justify-content: center; gap: 14px;
  }

  .event-wheel { position: absolute; left: 150px; top: 52px; width: 620px; height: 620px; }
  .price-badge {
    position: absolute; left: 460px; top: 362px; transform: translate(-50%, -50%);
    width: 230px; text-align: center; color: var(--pill-text);
  }
  .price-badge .lead { font: 900 13.5px "Lato", sans-serif; letter-spacing: .5px; }
  .price-badge .amount { font: 700 64px/1 "Oswald", sans-serif; color: var(--price-purple); margin: 4px 0 4px; }
  .price-badge .note { font: 900 13.5px/1.25 "Lato", sans-serif; letter-spacing: .3px; }

  .headline {
    position: absolute; left: 0; top: 700px; width: 100%; text-align: center;
    font: 900 108px/1 "Archivo", sans-serif; letter-spacing: 1px; color: var(--white);
    background: linear-gradient(180deg, #ffffff 0%, #ffffff 50%, #cfcfcf 100%);
    -webkit-background-clip: text; background-clip: text; -webkit-text-fill-color: transparent;
    filter: drop-shadow(0 3px 3px rgba(0,0,0,.35));
  }
  .subline {
    position: absolute; left: 0; top: 816px; width: 100%; text-align: center;
    font: 400 17px "Lato", sans-serif; color: var(--white); letter-spacing: .4px;
  }
  .rates-pill {
    position: absolute; left: 63px; top: 858px; width: 795px; height: 78px;
    background: var(--white); border-radius: 39px; box-shadow: 0 4px 8px rgba(0,0,0,.25);
    display: flex; align-items: center; justify-content: center; text-align: center;
    font: 700 23px/1.3 "Lato", sans-serif; color: var(--pill-text);
  }
  .rates-pill .rates { color: var(--price-green); }

  .packages { position: absolute; left: 169px; top: 962px; width: 700px; }
  .packages .title { position: absolute; left: 0; top: 0; font: 700 54px/1 "Oswald", sans-serif; color: var(--white); letter-spacing: .5px; text-shadow: 0 2px 3px rgba(0,0,0,.2); }
  .packages .attendant { position: absolute; left: 705px; top: 6px; writing-mode: vertical-rl; font: 700 11px "Oswald", sans-serif; color: var(--white); letter-spacing: .3px; }
  .packages .item { position: absolute; font-family: "Oswald", sans-serif; white-space: nowrap; }
  .item.filters { left: 0; top: 62px; font-weight: 700; font-size: 22px; color: var(--ink); }
  .item.green { left: 0; top: 91px; font-weight: 400; font-size: 17px; color: var(--white); }
  .item.props { left: 0; top: 113px; font-weight: 700; font-size: 26px; color: var(--ink); }
  .item.prints { left: 265px; top: 56px; font-weight: 500; font-size: 50px; line-height: 1; color: var(--ink); letter-spacing: .5px; }
  .item.strips { left: 265px; top: 117px; font-weight: 400; font-size: 17px; color: var(--white); }

  .footer-note { font: 700 11.5px "Oswald", sans-serif; color: var(--white); letter-spacing: .2px; }
  .footer-phone { display: flex; align-items: center; gap: 7px; font: 700 22px "Oswald", sans-serif; color: var(--white); }
</style>
</head>
<body>
<div class="flyer">
  <div class="top-band"></div>
  <div class="main-band"></div>

  <svg class="event-wheel" viewBox="-310 -310 620 620" aria-hidden="false">
    <defs>
      <linearGradient id="tone-a" x1="0" y1="0" x2="1" y2="1"><stop offset="0" stop-color="#e8d6cc"/><stop offset="1" stop-color="#b99486"/></linearGradient>
      <linearGradient id="tone-b" x1="0" y1="0" x2="1" y2="1"><stop offset="0" stop-color="#c0443e"/><stop offset="1" stop-color="#3a2a2a"/></linearGradient>
      <linearGradient id="tone-c" x1="0" y1="0" x2="1" y2="1"><stop offset="0" stop-color="#d9b8a0"/><stop offset="1" stop-color="#7a4f7e"/></linearGradient>
      <linearGradient id="tone-d" x1="0" y1="0" x2="1" y2="1"><stop offset="0" stop-color="#f0e6da"/><stop offset="1" stop-color="#4f5064"/></linearGradient>
      <linearGradient id="tone-e" x1="0" y1="0" x2="1" y2="1"><stop offset="0" stop-color="#e9c98a"/><stop offset="1" stop-color="#b57f68"/></linearGradient>
      <linearGradient id="tone-f" x1="0" y1="0" x2="1" y2="1"><stop offset="0" stop-color="#d5c7c0"/><stop offset="1" stop-color="#6e5a52"/></linearGradient>
      <linearGradient id="tone-g" x1="0" y1="0" x2="1" y2="1"><stop offset="0" stop-color="#efe6e2"/><stop offset="1" stop-color="#caa79a"/></linearGradient>
    </defs>
    <circle r="302" fill="#ffffff"/>
    <g stroke="#ffffff" stroke-width="9" stroke-linejoin="round">
      <path role="img" aria-label="Photo of a baby with a birthday cake" fill="url(#tone-g)" d="M0 0 L-123.4 -264.6 A292 292 0 0 1 130 -261.5 Z"/>
      <path role="img" aria-label="Photo of a bride and groom with friends" fill="url(#tone-b)" d="M0 0 L130 -261.5 A292 292 0 0 1 285.5 -61.4 Z"/>
      <path role="img" aria-label="Photo of women celebrating on a night out" fill="url(#tone-c)" d="M0 0 L285.5 -61.4 A292 292 0 0 1 226 184.9 Z"/>
      <path role="img" aria-label="Photo of colleagues toasting at a corporate event" fill="url(#tone-d)" d="M0 0 L226 184.9 A292 292 0 0 1 -3.6 292 Z"/>
      <path role="img" aria-label="Photo of a family at a kids birthday party" fill="url(#tone-e)" d="M0 0 L-3.6 292 A292 292 0 0 1 -230.4 179.4 Z"/>
      <path role="img" aria-label="Photo of friends posing together" fill="url(#tone-f)" d="M0 0 L-230.4 179.4 A292 292 0 0 1 -283.9 -68.5 Z"/>
      <path role="img" aria-label="Photo of guests smiling at a party" fill="url(#tone-a)" d="M0 0 L-283.9 -68.5 A292 292 0 0 1 -123.4 -264.6 Z"/>
    </g>
    <circle r="132" fill="#ffffff"/>
    <circle r="121" fill="#ffffff" stroke="#8869ae" stroke-width="8"/>
  </svg>

  <div class="price-badge">
    <p class="lead">PRICES START FROM</p>
    <p class="amount">$250</p>
    <p class="note">FOR KIDS PARTIES AND<br>DAY TIME EVENTS.</p>
  </div>

  <h1 class="headline">PHOTOBOOTH</h1>
  <p class="subline">WE ORGANISED WEDDINGS, BIRTHDAYS, CORPORATE EVENTS, HENS NIGHTS ECT.</p>

  <div class="rates-pill">
    <p><span class="rates">$450 - 3 hrs $550 - 4 hrs $650 - 5 hrs.</span> For extra time, additional<br>payment can be made on the night.</p>
  </div>

  <section class="packages">
    <h2 class="title">ALL PACKAGES INCLUDE</h2>
    <span class="attendant">PHOTOBOOTH ATTENDANT</span>
    <span class="item filters">CHOICE OF DIFFERENT FILTERS</span>
    <span class="item green">GREEN SCREEN TECHNOLOGY - OPTIONAL</span>
    <span class="item props">USE OF CHEEKY PROPS</span>
    <span class="item prints">UNLIMITED PRINTS</span>
    <span class="item strips">2 photo strips, one for you and one for friend.</span>
  </section>

  <footer class="footer-band">
    <span class="footer-note">CALL US FOR INFORMATION AND PRICES ON ADDITIONAL ITEMS LIKE PHOTO ALBUMS, MAGNETS, PERSONALIZED PHOTO STRIPS, AND MORE</span>
    <span class="footer-phone">
      <svg width="18" height="18" viewBox="0 0 18 18" aria-hidden="true">
        <rect width="18" height="18" rx="4" fill="#ffffff"/>
        <path d="M5 3.5c.6-.4 1.3-.3 1.6.3l1 1.8c.3.5.1 1.1-.3 1.4l-.7.5c.5 1.3 1.5 2.4 2.8 3l.5-.7c.3-.5.9-.6 1.4-.3l1.8 1c.6.3.7 1 .3 1.6l-.7.9c-.6.7-1.6.9-2.5.5C7.3 12.4 5.5 10.6 4.4 7.7 4 6.8 4.2 5.8 4.9 5.1z" fill="#111"/>
      </svg>
      0461927584
    </span>
  </footer>
</div>
</body>
</html>
```